fernbolt website

commerce website to sell cookeries, brackets, mailboxes and to show off homes built. Modern Steel in design see kelvo rides web page to be like: https://www.kelvorides.com/en/ sorry its blue mantis hosting word press divi

must be able to add products to page

Target Market(s)

mainly western states of U.S.

Industry/Entity Type

Building Product

Coding

Coded - Design and coding required

Number of Pages Required

3 page

Font styles to use
Sans Serif

Colors

Designer to choose colors to be used in the design.

Requirements
Must have
• customers to be able to order products from page
• blue mantis hosting word press divi

```html
<!DOCTYPE html>
<html lang="en">
<head>
<meta charset="utf-8">
<title>Fernbolt — Steel Products</title>
<link rel="stylesheet" href="https://fonts.googleapis.com/css2?family=Poppins:wght@400;500&family=Roboto+Condensed:ital,wght@1,400&display=swap">
<style>
  :root {
    --steel-blue: #4b5e87;
    --steel-blue-light: #5d6f99;
    --ink: #2b2b2b;
    --white: #ffffff;
    --rule: #4b5e87;
    --faint: #eef0f5;
    --black: #0d0d0d;
  }
  * { margin: 0; padding: 0; box-sizing: border-box; }
  html, body { width: 741px; height: 1200px; overflow: hidden; }
  body { position: relative; background: var(--white); font-family: 'Poppins', sans-serif; color: var(--ink); }
  .abs { position: absolute; }

  /* Header */
  .site-header { position: absolute; left: 0; top: 0; width: 741px; height: 71px; background: var(--steel-blue); color: var(--white); }
  .brand { position: absolute; left: 89px; top: 22px; display: flex; align-items: center; gap: 7px; font-size: 17px; font-weight: 500; letter-spacing: 1px; color: var(--white); }
  .brand-dot { width: 14px; height: 14px; border-radius: 50%; background: var(--white); }
  .top-contact { position: absolute; top: 11px; font-size: 8.5px; display: flex; align-items: center; gap: 5px; }
  .top-contact svg { width: 12px; height: 12px; }
  .top-divider { position: absolute; left: 522px; top: 13px; width: 1px; height: 10px; background: rgba(255,255,255,.35); }
  .main-nav a { position: absolute; top: 44px; font-size: 10px; color: var(--white); text-decoration: none; }
  .main-nav a.active { font-weight: 500; border-bottom: 1px solid var(--white); padding-bottom: 1px; }

  /* Hero */
  .hero { position: absolute; left: 0; top: 71px; width: 741px; height: 340px;
    background: linear-gradient(180deg, #9fb6cf 0%, #7f95a6 35%, #5d6a62 65%, #8c7a5f 100%); }
  .hero-title { position: absolute; left: 90px; top: 137px; width: 560px; text-align: center; font-size: 21.5px; font-weight: 500; line-height: 30px; color: var(--white); text-shadow: 0 1px 4px rgba(0,0,0,.6); }

  /* Products */
  .section-title { position: absolute; left: 0; top: 446px; width: 741px; text-align: center; font-size: 24px; font-weight: 400; color: var(--steel-blue); }
  .title-rule { position: absolute; height: 1.5px; background: var(--rule); }
  .intro { position: absolute; left: 95px; top: 492px; width: 551px; text-align: center; font-size: 9.8px; line-height: 17.5px; }
  .product-card { position: absolute; top: 536px; width: 180px; height: 217px; background: var(--white); box-shadow: 0 3px 6px rgba(0,0,0,.16); }
  .product-photo { width: 180px; height: 143px; }
  .product-name { text-align: center; font-size: 13px; margin-top: 7px; }
  .product-rule { width: 30px; height: 1.5px; background: var(--rule); margin: 5px auto 8px; }
  .product-text { text-align: center; font-size: 8px; line-height: 14.5px; padding: 0 5px; }
  .shop-btn { position: absolute; left: 318px; top: 776px; width: 105px; height: 25px; border-radius: 13px; background: var(--steel-blue); color: var(--white); font-size: 10px; font-weight: 500; display: flex; align-items: center; justify-content: center; gap: 6px; }
  .shop-btn .dot { width: 9px; height: 9px; border-radius: 50%; background: var(--white); }

  /* Goal */
  .goal-text { position: absolute; left: 120px; top: 910px; width: 501px; text-align: center; font-family: 'Roboto Condensed', sans-serif; font-style: italic; font-size: 24.5px; line-height: 31px; color: #333; text-transform: uppercase; }

  /* Footer */
  .footer-nav { position: absolute; left: 0; top: 1062px; width: 741px; height: 29px; background: var(--steel-blue-light); }
  .footer-nav a { position: absolute; top: 8px; font-size: 9px; color: var(--white); text-decoration: none; }
  .footer-main { position: absolute; left: 0; top: 1091px; width: 741px; height: 83px; background: var(--steel-blue); color: var(--white); }
  .footer-brand { position: absolute; left: 112px; top: 33px; display: flex; align-items: center; gap: 6px; font-size: 14px; font-weight: 500; letter-spacing: 1px; }
  .footer-divider { position: absolute; top: 28px; width: 1px; height: 35px; background: rgba(255,255,255,.3); }
  .footer-contact { position: absolute; top: 32px; font-size: 9px; line-height: 13px; }
  .footer-contact svg { position: absolute; left: -18px; top: 3px; width: 13px; height: 13px; }
  .social { position: absolute; top: 1127px; width: 18px; height: 18px; border: 1px solid var(--white); border-radius: 50%; }
  .copyright { position: absolute; left: 0; top: 1174px; width: 741px; height: 26px; background: var(--black); color: var(--white); font-size: 7px; text-align: center; line-height: 26px; }
</style>
</head>
<body>

<header class="site-header">
  <div class="brand"><span class="brand-dot"></span>FERNBOLT</div>
  <div class="top-contact" style="left:434px">
    <svg viewBox="0 0 24 24" fill="none" stroke="#fff" stroke-width="1.6"><path d="M5 3h4l2 5-2.5 1.5a11 11 0 0 0 6 6L16 13l5 2v4a2 2 0 0 1-2 2A16 16 0 0 1 3 5a2 2 0 0 1 2-2z"/></svg>
    555.014.2288
  </div>
  <div class="top-divider"></div>
  <div class="top-contact" style="left:536px">
    <svg viewBox="0 0 24 24" fill="none" stroke="#fff" stroke-width="1.6"><rect x="3" y="6" width="18" height="13"/><path d="M3 6l9 7 9-7"/></svg>
    inquiry@fernbolt.com
  </div>
  <nav class="main-nav">
    <a class="active" href="#" style="left:345px">Home</a>
    <a href="#" style="left:397px">Products</a>
    <a href="#" style="left:461px">Home Built</a>
    <a href="#" style="left:534px">About Us</a>
    <a href="#" style="left:599px">Contact Us</a>
  </nav>
</header>

<section class="hero" role="img" aria-label="Photo of a modern steel-clad house with large windows under a blue sky with palm trees">
  <h1 class="hero-title">We Sell Cookeries, Brackets, Mailboxes And To Show Off Homes Built</h1>
</section>

<section class="products">
  <h2 class="section-title">Our Products</h2>
  <div class="title-rule" style="left:356px;top:479px;width:30px"></div>
  <p class="intro">Lorem ipsum dolor sit amet, consectetuer adipiscing elit, sed diam nonummy nibh euismod tincidunt ut laoreet dolore magna aliquam erat volutpat Ut wisi enim ad minim.</p>

  <article class="product-card" style="left:87px">
    <div class="product-photo" role="img" aria-label="Photo of dark steel wall panels beside a glass sliding door" style="background:linear-gradient(135deg,#2e3236,#6b6f72 60%,#3d4144)"></div>
    <h3 class="product-name">Steel Cookery</h3>
    <div class="product-rule"></div>
    <p class="product-text">Lorem ipsum dolor sit amet, consectetuer adipiscing elit, sed diam</p>
  </article>
  <article class="product-card" style="left:281px">
    <div class="product-photo" role="img" aria-label="Photo of a modern steel house exterior" style="background:linear-gradient(180deg,#a9bfd6,#6f7c80 55%,#9c8663)"></div>
    <h3 class="product-name">Brackets</h3>
    <div class="product-rule"></div>
    <p class="product-text">Lorem ipsum dolor sit amet, consectetuer adipiscing elit, sed diam</p>
  </article>
  <article class="product-card" style="left:474px">
    <div class="product-photo" role="img" aria-label="Photo of a round steel fire table in a workshop" style="background:linear-gradient(180deg,#8c8d8c,#5a5a5a 60%,#7e7c78)"></div>
    <h3 class="product-name">Mail Boxes</h3>
    <div class="product-rule"></div>
    <p class="product-text">Lorem ipsum dolor sit amet, consectetuer adipiscing elit, sed diam</p>
  </article>

  <div class="shop-btn"><span class="dot"></span>SHOP NOW</div>
</section>

<section class="goal">
  <div class="title-rule" style="left:134px;top:881px;width:212px"></div>
  <div class="title-rule" style="left:395px;top:881px;width:212px"></div>
  <svg class="abs" style="left:353px;top:868px" width="36" height="28" viewBox="0 0 36 28" fill="none" stroke="#4b5e87">
    <circle cx="23" cy="14" r="11" stroke-width="2.4"/>
    <circle cx="23" cy="14" r="6" stroke-width="2"/>
    <circle cx="23" cy="14" r="2" fill="#4b5e87" stroke="none"/>
    <path d="M2 8l21 6" stroke-width="2"/>
    <path d="M2 4l5 4-5 3z" fill="#4b5e87" stroke="none"/>
  </svg>
  <p class="goal-text">Our goal is simply to build the best products in the world</p>
  <div class="title-rule" style="left:134px;top:982px;width:473px"></div>
</section>

<nav class="footer-nav">
  <a href="#" style="left:208px">Home</a>
  <a href="#" style="left:260px">Products</a>
  <a href="#" style="left:325px">Home Built</a>
  <a href="#" style="left:398px">About Us</a>
  <a href="#" style="left:463px">Contact Us</a>
</nav>

<footer class="footer-main">
  <div class="footer-brand"><span class="brand-dot" style="width:11px;height:11px"></span>FERNBOLT</div>
  <div class="footer-divider" style="left:222px"></div>
  <div class="footer-contact" style="left:268px">
    <svg viewBox="0 0 24 24" fill="none" stroke="#fff" stroke-width="1.6"><rect x="3" y="6" width="18" height="13"/><path d="M3 6l9 7 9-7"/></svg>
    Email Us<br>inquiry@fernbolt.com
  </div>
  <div class="footer-divider" style="left:400px"></div>
  <div class="footer-contact" style="left:452px">
    <svg viewBox="0 0 24 24" fill="none" stroke="#fff" stroke-width="1.6"><path d="M5 3h4l2 5-2.5 1.5a11 11 0 0 0 6 6L16 13l5 2v4a2 2 0 0 1-2 2A16 16 0 0 1 3 5a2 2 0 0 1 2-2z"/></svg>
    Call Us On<br>555.014.2288
  </div>
  <div class="footer-divider" style="left:545px"></div>
</footer>
<span class="social" style="left:573px"></span>
<span class="social" style="left:594px"></span>
<span class="social" style="left:615px"></span>

<div class="copyright">Copyright © 2020 Fernbolt. All Rights Reserved.</div>

</body>
</html>
```